Bring me business with this creative business card

Design my new business card. I am looking for something different with an impact. People will take a look at this card & they will 1- see how different & creative I am, 2-understand what I do 3- Call me to meet me!

I make videos with a message, testimonials. I am dynamic, fun, creative & human. My new website is in construction but in the meantime you can check this old one: brightpath.ca & another one Fernquill.com & fernquill facebook page.
I make videos. sometimes with a cameraman, sometimes with my phone. As an ex Public Relations agent, the message is the most important thing for me. I want to make my clients shine! When they start with me they often remind me of a lamb, when I finish coaching them they are powerful like LIONS! That's why I need a powerful business card!

Target Market(s)

Entrepreneurs, solo entrepreneurs, small & medium companies & start ups. People i will meet while networking. People that need videos on their website & social Networks to get attention, to be visible. men & women. From 35 to 49 years old.
I am an ex Public relations agent. I used to send clients in traditional medias, now with videos they have more chances to be seen on google the new media. I do videos of the president, his team, his loyal clients saying how great the company is & expert videos like series so people can be seen for example every 1 st of every month with a short 2 minute video. Also with my 20 years in marketing & communications I can coach & give tips to anybody who needs it.
Target: anybody who would like my old website brightpath.ca & I also have another website but it will be off line soon: fernquill.com could give you ideas.

Industry/Entity Type

Communications

Contact Information for Business Card

I am in Montreal,So the business cards have to be the usual size like we have in Montreal: 9 cm x 5 cm
Details:My text: Corinne Vautrin Communication coach/Head Storyteller. "Crafting Videos as bold as you are" off: 514-555-0147 cell: 514-555-0183. fernquill.com
corinne@fernquill.com logo facebook, youtube, instagram

Colors
f37122

Requirements
Must have
• Dynamic, happy. Orange. Be creative in the look but NOT the shape of the card. Easy to read. Big enough to read.
Should not have
• No funny shapes: no round, no square, just the usual. I love creative but NOT on shape.

```html
<!DOCTYPE html>
<html lang="en">
<head>
<meta charset="utf-8">
<title>Fernquill Business Card</title>
<link href="https://fonts.googleapis.com/css2?family=Comfortaa:wght@500&family=Open+Sans:wght@600;700&display=swap" rel="stylesheet">
<style>
  :root {
    --stage: #0f7fbe;
    --stage-dark: #0a5f8f;
    --orange: #f26b22;
    --amber: #f7931e;
    --yellow: #f9d30f;
    --vermilion: #f05a28;
    --charcoal: #323031;
    --ink: #1f1f1f;
    --white: #ffffff;
    --emblem-light: #fbd423;
    --emblem-mid: #f7941d;
    --emblem-dark: #ef5a24;
  }
  * { box-sizing: border-box; margin: 0; padding: 0; }
  html, body { width: 1200px; height: 1000px; overflow: hidden; }
  body {
    position: relative;
    background: radial-gradient(ellipse at 30% 45%, var(--stage) 0%, var(--stage) 45%, var(--stage-dark) 100%);
    font-family: "Open Sans", Arial, sans-serif;
  }
  .card {
    position: absolute;
    left: 245px;
    width: 710px;
    height: 394px;
    overflow: hidden;
  }
  .card--front { top: 78px; background: var(--charcoal); }
  .card--back { top: 528px; background: var(--white); }

  .stripe {
    position: absolute;
    left: 0;
    width: 100%;
    height: 35px;
    display: flex;
  }
  .stripe--top { top: 0; }
  .stripe--bottom { bottom: 0; }
  .stripe span:nth-child(1) { width: 166px; background: var(--orange); }
  .stripe span:nth-child(2) { width: 190px; background: var(--amber); }
  .stripe span:nth-child(3) { width: 189px; background: var(--yellow); }
  .stripe span:nth-child(4) { flex: 1; background: var(--vermilion); }

  .emblem {
    position: absolute;
    background: radial-gradient(ellipse at 50% 60%, var(--emblem-light) 0%, var(--emblem-mid) 50%, var(--emblem-dark) 100%);
    border-radius: 22% 22% 42% 42% / 18% 18% 50% 50%;
  }
  .card--front .emblem {
    left: 275px; top: 77px; width: 168px; height: 205px;
    border: 2px solid var(--white);
  }
  .tagline {
    position: absolute;
    top: 317px;
    width: 100%;
    text-align: center;
    font-family: "Comfortaa", "Quicksand", sans-serif;
    font-weight: 500;
    font-size: 22px;
    color: var(--white);
  }

  .identity { position: absolute; left: 22px; top: 80px; }
  .identity__name {
    font-weight: 700;
    font-size: 28px;
    color: var(--orange);
    letter-spacing: 0.5px;
    line-height: 1.1;
  }
  .identity__role {
    font-weight: 600;
    font-size: 21px;
    color: var(--ink);
    margin-top: 3px;
  }
  .contacts {
    position: absolute;
    left: 23px;
    top: 165px;
    list-style: none;
  }
  .contacts li {
    display: flex;
    align-items: center;
    height: 39px;
    font-weight: 600;
    font-size: 21px;
    color: var(--ink);
  }
  .contacts svg { width: 32px; height: 26px; margin-right: 11px; flex: none; }

  .brand { position: absolute; left: 480px; top: 0; width: 214px; height: 100%; }
  .brand .emblem { left: 60px; top: 79px; width: 95px; height: 118px; }
  .brand__name {
    position: absolute;
    top: 204px;
    width: 100%;
    text-align: center;
    font-weight: 700;
    font-size: 29px;
    color: var(--orange);
    letter-spacing: 1px;
  }
  .social { position: absolute; top: 272px; left: 24px; display: flex; gap: 7px; }
  .social span {
    width: 49px; height: 49px;
    border-radius: 50%;
    background: var(--vermilion);
  }
</style>
</head>
<body>

<section class="card card--front">
  <div class="stripe stripe--top"><span></span><span></span><span></span><span></span></div>
  <div class="emblem" role="img" aria-label="Geometric low-poly animal head illustration in orange and yellow"></div>
  <p class="tagline">“Crafting Videos as bold as you are”</p>
  <div class="stripe stripe--bottom"><span></span><span></span><span></span><span></span></div>
</section>

<section class="card card--back">
  <div class="stripe stripe--top"><span></span><span></span><span></span><span></span></div>

  <div class="identity">
    <h1 class="identity__name">CORINNE VAUTRIN</h1>
    <p class="identity__role">Communication coach/Head Storyteller</p>
  </div>

  <ul class="contacts">
    <li>
      <svg viewBox="0 0 32 26" aria-hidden="true"><rect width="32" height="26" rx="8" fill="#f05a28"/><path d="M12 6c1 0 2 2.5 2 3.5s-1.5 1.2-1 2.5 2 3 3.2 3.4 1.3-1 2.3-1 3.5 1 3.5 2-1.5 2.6-3 2.6C14 19 9 13.5 9 9c0-1.5 2-3 3-3z" fill="#fff"/></svg>
      514-555-0147
    </li>
    <li>
      <svg viewBox="0 0 32 26" aria-hidden="true"><rect width="32" height="26" rx="8" fill="#f05a28"/><rect x="11.5" y="4.5" width="9" height="17" rx="1.5" fill="none" stroke="#fff" stroke-width="2"/><circle cx="16" cy="18.5" r="1" fill="#fff"/></svg>
      514-555-0183
    </li>
    <li>
      <svg viewBox="0 0 32 26" aria-hidden="true"><rect width="32" height="26" rx="8" fill="#f05a28"/><rect x="8" y="6" width="16" height="10.5" rx="1" fill="none" stroke="#fff" stroke-width="2"/><path d="M13 20h6M16 17v3" stroke="#fff" stroke-width="2"/></svg>
      www.fernquill.com
    </li>
    <li>
      <svg viewBox="0 0 32 26" aria-hidden="true"><rect width="32" height="26" rx="8" fill="#f05a28"/><rect x="8" y="7" width="16" height="12" fill="#fff"/><path d="M8 7l8 6.5L24 7" fill="none" stroke="#f05a28" stroke-width="1.6"/></svg>
      corinne@fernquill.com
    </li>
  </ul>

  <div class="brand">
    <div class="emblem" role="img" aria-label="Small geometric animal head illustration"></div>
    <p class="brand__name">FERNQUILL</p>
    <div class="social" role="img" aria-label="Social media links">
      <span></span><span></span><span></span>
    </div>
  </div>

  <div class="stripe stripe--bottom"><span></span><span></span><span></span><span></span></div>
</section>

</body>
</html>
```